Looking for an Innovative Print Design (Service Directory)

We need a new design for our advertisement within a printed colour services directory.

We are a compensation law firm called Velbrook Compensation Lawyers. Feel free to take a browse of our website www.velbrooklegal.com.au to get an idea of what we do and the kind of firm we are.

We are in the process of redeveloping our website and as such, so please don't adhere to the design principles of the current site- impress us with your originality!

On top of any editable formats, your final submissions must include a .pdf copy.
The same design will need to be presented in two dimensions:

- 154mm x 118mm (B1/B2 Half Page);
- 175mm x 113mm (B4 Half Page).

[For more information refer to attached Pdf.]

We have attached for you a few examples of other firms' designs (Sample1,2,3). These are by no means good, or what we're after, it's just to provide you with an idea of what sort of advertisements go into the service directory.

Hi all,

We want to emphasise that a priority of the design is that it must look:
• Professional
• Sophisticated
Please do not hesitate to use completely different colour schemes to the ones that are on our website- as we have said, our website will change in the near future, so cohesion between the current project and the website is not necessary!

Thanks!

Thank you for your submissions so far. There are some great ideas hidden in there. 

An issue we are having is that most of you are conforming to the same understanding of what it should look like. Remember that there is NO NEED to be bound by the image of firm as is. That is, feel free to use a different colour logo.

For inspiration, we relate well to the design aesthetics of: http://www.tinfernstudio.co.uk/

Look forward to seeing your 'out of the box' submissions. 

Reason: We've received a large amount of fantastic designs. However, what we're really looking for is something original. Please feel free to think outside the box (the final design doesn't need to look like a print ad), and construct a design that is completely incongruous with our website! While we do appreciate a minimalistic design, we have yet to receive something that really grabs your attention with its visuals. We're not sure but this may or may not be achieved with a full colour design. Thanks for all your submissions- they all have some features that really click with us. We look forward to the next wave of submissions!

Target Market(s)

We have various target markets, including mainly families, elderly people, blue collar workers.

These are individuals who are looking for assistance. They feel helpless or wronged.

Keep in mind that the people accessing these are those who prefer going to a printed directory rather than using a google search.

Industry/Entity Type

Law Firm

Font styles to use
Serif
Sans Serif

Requirements
Must have
• - Our name 'Velbrook Compensation Lawyers'
- Our logo (attached as logo.eps, logo.png, and logo.tif)
- Must include phone number as 1300 XXX XXX (this must be prominent)
- Must include the following service areas in these words: Motor vehicle claims, medical claims, superannuation claims, Workplace claims, negligence claims
- Our email address: info@velbrooklegal.com.au
- Our website address: www.velbrooklegal.com.au
- The following catchphrases: '98% success rate', and 'No win no fee' in those words
- Our location '412 Carvel Lane, Smithville, SYDNEY'
- For sizing dimensions, we need one in 154mm x 118mm and also a design in 175mm x 113mm (B4 Half Page) [refer to pdf attached]
Nice to have
• - Text indicating free initial consulatation
- Professional colour scheme
- As our website will be changed, do not worry about making the advertisement cohesive with our website design
- We want the design to be modern, but still professional
- Clean typeface
- No gradient colour scheme
- When designing, if you are looking to place more text onto the advertisement, these may be some considerations (feel free to change the wording): Accredited specialists, home and hospital visits

```html
<!DOCTYPE html>
<html lang="en">
<head>
<meta charset="utf-8">
<title>Velbrook Compensation Lawyers – Directory Advertisement</title>
<link rel="stylesheet" href="https://fonts.googleapis.com/css2?family=EB+Garamond:wght@600;700&family=Montserrat:wght@300;600&family=Open+Sans:wght@600;700&display=swap">
<style>
  :root {
    --page: #ffffff;
    --wine-light: #a81e25;
    --wine: #8c161c;
    --wine-dark: #4f080c;
    --ink-white: #ffffff;
    --brand-orange: #ee6a24;
    --phone-gold: #f6dc9f;
    --seal-gold: #b8902e;
    --seal-gold-dark: #8a6a1c;
    --tick-red: #d9262b;
    --card-edge: #3a0a0c;
  }
  * { margin: 0; padding: 0; box-sizing: border-box; }
  html, body {
    width: 898px; height: 1200px; overflow: hidden;
    background: var(--page);
  }
  .sheet { position: relative; width: 898px; height: 1200px; }

  .ad {
    position: absolute;
    border: 1px solid var(--card-edge);
    background: radial-gradient(ellipse at 40% 50%, var(--wine-light) 0%, var(--wine) 45%, var(--wine-dark) 100%);
    overflow: hidden;
    color: var(--ink-white);
  }
  .ad--half-b1 { left: 93px; top: 40px; width: 687px; height: 528px; }
  .ad--half-b4 { left: 56px; top: 632px; width: 782px; height: 505px; }

  .brand-dot {
    position: absolute; border-radius: 50%;
    background: var(--brand-orange);
  }
  .brand-name {
    position: absolute;
    font-family: "Montserrat", sans-serif; font-weight: 300;
    font-size: 74px; line-height: 1; letter-spacing: 3px;
    text-shadow: 0 2px 4px rgba(0,0,0,.35);
  }
  .brand-tagline {
    position: absolute;
    font-family: "Montserrat", sans-serif; font-weight: 600;
    font-size: 21px; line-height: 1; letter-spacing: 2.6px;
    text-shadow: 0 1px 3px rgba(0,0,0,.35);
  }

  .services { position: absolute; list-style: none; }
  .service {
    position: relative; height: 39.5px; line-height: 39.5px;
    font-family: "EB Garamond", serif; font-weight: 600; font-size: 29px;
    text-shadow: 1px 2px 3px rgba(0,0,0,.55);
    white-space: nowrap;
  }
  .service__tick {
    position: absolute; top: 7px; width: 30px; height: 28px;
    filter: drop-shadow(1px 2px 2px rgba(0,0,0,.5));
  }
  .service__tick path { fill: none; stroke-linecap: round; stroke-linejoin: round; }
  .service__tick .tick-edge { stroke: var(--ink-white); stroke-width: 6; }
  .service__tick .tick-mark { stroke: var(--tick-red); stroke-width: 3.4; }

  .phone {
    position: absolute;
    font-family: "EB Garamond", serif; font-weight: 700;
    font-size: 54px; line-height: 1; letter-spacing: .5px;
    color: var(--phone-gold);
    text-shadow: 1px 2px 4px rgba(0,0,0,.55);
  }

  .seal { position: absolute; width: 252px; height: 252px; }
  .seal svg { position: absolute; inset: 0; filter: drop-shadow(2px 4px 5px rgba(0,0,0,.45)); }
  .seal__text {
    position: absolute; inset: 0;
    display: flex; flex-direction: column; align-items: center; justify-content: center;
    transform: rotate(14deg);
    font-family: "Open Sans", sans-serif; text-align: center;
    text-shadow: 1px 2px 3px rgba(0,0,0,.45);
  }
  .seal__rate { font-weight: 700; font-size: 38px; line-height: 1.02; }
  .seal__offer { font-weight: 600; font-size: 16px; margin-top: 8px; }

  .contact {
    position: absolute;
    font-family: "Open Sans", sans-serif; font-size: 15.5px; line-height: 1;
    text-shadow: 0 1px 2px rgba(0,0,0,.4);
    white-space: nowrap;
  }
  .contact--web { font-weight: 700; }
  .contact--address { left: 0; right: 0; text-align: center; }
</style>
</head>
<body>
<main class="sheet">

  <!-- B1/B2 half page -->
  <section class="ad ad--half-b1" aria-label="Velbrook Compensation Lawyers advertisement, 154 by 118 mm">
    <div class="brand-dot" style="left:86px;top:32px;width:108px;height:108px"></div>
    <div class="brand-name" style="left:213px;top:46px">VELBROOK</div>
    <div class="brand-tagline" style="left:216px;top:123px">COMPENSATION LAWYERS</div>

    <ul class="services" style="left:41px;top:183px">
      <li class="service"><svg class="service__tick" viewBox="0 0 30 28" style="left:0"><path class="tick-edge" d="M5 15 L12 23 C16 14 21 8 27 4"/><path class="tick-mark" d="M5 15 L12 23 C16 14 21 8 27 4"/></svg><span style="margin-left:46px">Motor vehicle claims</span></li>
      <li class="service"><svg class="service__tick" viewBox="0 0 30 28" style="left:0"><path class="tick-edge" d="M5 15 L12 23 C16 14 21 8 27 4"/><path class="tick-mark" d="M5 15 L12 23 C16 14 21 8 27 4"/></svg><span style="margin-left:46px">Medical claims</span></li>
      <li class="service"><svg class="service__tick" viewBox="0 0 30 28" style="left:0"><path class="tick-edge" d="M5 15 L12 23 C16 14 21 8 27 4"/><path class="tick-mark" d="M5 15 L12 23 C16 14 21 8 27 4"/></svg><span style="margin-left:46px">Superannuation claims</span></li>
      <li class="service"><svg class="service__tick" viewBox="0 0 30 28" style="left:0"><path class="tick-edge" d="M5 15 L12 23 C16 14 21 8 27 4"/><path class="tick-mark" d="M5 15 L12 23 C16 14 21 8 27 4"/></svg><span style="margin-left:46px">Workplace claims</span></li>
      <li class="service"><svg class="service__tick" viewBox="0 0 30 28" style="left:0"><path class="tick-edge" d="M5 15 L12 23 C16 14 21 8 27 4"/><path class="tick-mark" d="M5 15 L12 23 C16 14 21 8 27 4"/></svg><span style="margin-left:46px">Negligence claims</span></li>
    </ul>

    <div class="phone" style="left:38px;top:398px">1300 XXX XXX</div>

    <div class="seal" style="left:409px;top:176px">
      <svg viewBox="-100 -100 200 200" aria-hidden="true">
        <g fill="var(--seal-gold)">
          <circle r="87"/>
          <rect x="-70.7" y="-70.7" width="141.4" height="141.4"/>
          <rect x="-70.7" y="-70.7" width="141.4" height="141.4" transform="rotate(15)"/>
          <rect x="-70.7" y="-70.7" width="141.4" height="141.4" transform="rotate(30)"/>
          <rect x="-70.7" y="-70.7" width="141.4" height="141.4" transform="rotate(45)"/>
          <rect x="-70.7" y="-70.7" width="141.4" height="141.4" transform="rotate(60)"/>
          <rect x="-70.7" y="-70.7" width="141.4" height="141.4" transform="rotate(75)"/>
        </g>
      </svg>
      <div class="seal__text">
        <span class="seal__rate">98%<br>Success<br>Rate!</span>
        <span class="seal__offer">No Win No Fee</span>
      </div>
    </div>

    <div class="contact contact--email" style="left:62px;top:466px">info@velbrooklegal.com.au</div>
    <div class="contact contact--web" style="left:357px;top:466px">www.velbrooklegal.com.au</div>
    <div class="contact contact--address" style="top:491px">412 Carvel Lane, Smithville, SYDNEY</div>
  </section>

  <!-- B4 half page -->
  <section class="ad ad--half-b4" aria-label="Velbrook Compensation Lawyers advertisement, 175 by 113 mm">
    <div class="brand-dot" style="left:99px;top:44px;width:105px;height:105px"></div>
    <div class="brand-name" style="left:247px;top:52px">VELBROOK</div>
    <div class="brand-tagline" style="left:249px;top:120px">COMPENSATION LAWYERS</div>

    <ul class="services" style="left:63px;top:175px">
      <li class="service"><svg class="service__tick" viewBox="0 0 30 28" style="left:0"><path class="tick-edge" d="M5 15 L12 23 C16 14 21 8 27 4"/><path class="tick-mark" d="M5 15 L12 23 C16 14 21 8 27 4"/></svg><span style="margin-left:47px">Motor vehicle claims</span></li>
      <li class="service"><svg class="service__tick" viewBox="0 0 30 28" style="left:0"><path class="tick-edge" d="M5 15 L12 23 C16 14 21 8 27 4"/><path class="tick-mark" d="M5 15 L12 23 C16 14 21 8 27 4"/></svg><span style="margin-left:47px">Medical claims</span></li>
      <li class="service"><svg class="service__tick" viewBox="0 0 30 28" style="left:0"><path class="tick-edge" d="M5 15 L12 23 C16 14 21 8 27 4"/><path class="tick-mark" d="M5 15 L12 23 C16 14 21 8 27 4"/></svg><span style="margin-left:47px">Superannuation claims</span></li>
      <li class="service"><svg class="service__tick" viewBox="0 0 30 28" style="left:0"><path class="tick-edge" d="M5 15 L12 23 C16 14 21 8 27 4"/><path class="tick-mark" d="M5 15 L12 23 C16 14 21 8 27 4"/></svg><span style="margin-left:47px">Workplace claims</span></li>
      <li class="service"><svg class="service__tick" viewBox="0 0 30 28" style="left:0"><path class="tick-edge" d="M5 15 L12 23 C16 14 21 8 27 4"/><path class="tick-mark" d="M5 15 L12 23 C16 14 21 8 27 4"/></svg><span style="margin-left:47px">Negligence claims</span></li>
    </ul>

    <div class="phone" style="left:60px;top:388px">1300 XXX XXX</div>

    <div class="seal" style="left:482px;top:142px">
      <svg viewBox="-100 -100 200 200" aria-hidden="true">
        <g fill="var(--seal-gold)">
          <circle r="87"/>
          <rect x="-70.7" y="-70.7" width="141.4" height="141.4"/>
          <rect x="-70.7" y="-70.7" width="141.4" height="141.4" transform="rotate(15)"/>
          <rect x="-70.7" y="-70.7" width="141.4" height="141.4" transform="rotate(30)"/>
          <rect x="-70.7" y="-70.7" width="141.4" height="141.4" transform="rotate(45)"/>
          <rect x="-70.7" y="-70.7" width="141.4" height="141.4" transform="rotate(60)"/>
          <rect x="-70.7" y="-70.7" width="141.4" height="141.4" transform="rotate(75)"/>
        </g>
      </svg>
      <div class="seal__text">
        <span class="seal__rate">98%<br>Success<br>Rate!</span>
        <span class="seal__offer">No Win No Fee</span>
      </div>
    </div>

    <div class="contact contact--email" style="left:111px;top:449px">info@velbrooklegal.com.au</div>
    <div class="contact contact--web" style="left:405px;top:449px">www.velbrooklegal.com.au</div>
    <div class="contact contact--address" style="top:473px">412 Carvel Lane, Smithville, SYDNEY</div>
  </section>

</main>
</body>
</html>
```